Peter Lanford Studios Business Card

Looking for a clear, modern, elegant, sharp business card that conveys a professional yet edgy image to my business as a wedding, portrait, and travel photographer. Would like something that looks vintage yet modern. Need a new business card to grow my business. We are growing the business for Wedding and Event Photography as well as fine art Photography. (Mostly Landscapes)
Updates

I’m looking through designs now but I have a new logo that i want using please.

New logo uploaded please redesign using that

PLEASE ALL DESIGNERS LOOK IN BRIEF FOR NEW LOGO

Target Market(s)

Brides, Grooms, Families with Kids, People looking for Fine Art Photography Artwork

Industry/Entity Type

Photographer

Contact Information for Business Card

Unsure

Font styles to use
Serif

Colors

Designer to choose colors to be used in the design.

Requirements
Must have
• My Website:
• http://lanfordgallery.snapfolio.example
• Phone:
• 555-418-2061
• Email:
• petelanfordgallery@mailbox.example
Nice to have
• Would like a sort of shine on the printing finish.
• I like black I think it looks good on a business card.
• Can try working with my logo (png that I've attached)

```html
<!DOCTYPE html>
<html lang="en">
<head>
<meta charset="utf-8">
<title>Peter Lanford Studios – Business Card</title>
<link rel="stylesheet" href="https://fonts.googleapis.com/css2?family=Josefin+Sans:wght@300;400&family=Pinyon+Script&display=swap">
<style>
  :root {
    --backdrop: #2b2724;
    --card: #121212;
    --card-edge: #1c1c1c;
    --silver: #e4e4e4;
    --silver-soft: #bdbdbd;
    --silver-dim: #8c8c8c;
    --rule: #cfcfcf;
  }
  * { box-sizing: border-box; margin: 0; padding: 0; }
  html, body { width: 1200px; height: 769px; overflow: hidden; }
  body {
    background: var(--backdrop);
    font-family: "Josefin Sans", sans-serif;
    color: var(--silver);
    position: relative;
  }
  .card {
    position: absolute;
    top: 230px;
    width: 540px;
    height: 310px;
    background: var(--card);
    border: 1px solid var(--card-edge);
    box-shadow: 0 18px 40px rgba(0,0,0,.45);
  }
  .card--front { left: 40px; }
  .card--back { left: 620px; }

  /* Front */
  .brand {
    position: absolute;
    top: 34px;
    left: 0;
    width: 100%;
    text-align: center;
  }
  .brand__mark {
    display: block;
    width: 46px;
    height: 46px;
    margin: 0 auto 14px;
    border: 1.5px solid var(--silver);
  }
  .brand__name {
    font-weight: 300;
    font-size: 30px;
    letter-spacing: 1px;
    line-height: 1;
    color: var(--silver);
  }
  .brand__sub {
    margin-top: 6px;
    font-weight: 300;
    font-size: 11px;
    letter-spacing: 9px;
    padding-left: 9px;
    color: var(--silver);
  }
  .rule {
    position: absolute;
    height: 1px;
    background: var(--rule);
  }
  .rule--top { top: 178px; left: 170px; right: 22px; }
  .rule--bottom { top: 262px; left: 22px; right: 22px; }
  .person {
    position: absolute;
    top: 202px;
    left: 90px;
    display: flex;
    align-items: baseline;
    gap: 22px;
    font-weight: 300;
    color: var(--silver-dim);
  }
  .person__name { font-size: 22px; }
  .person__dash { font-size: 16px; color: var(--silver-soft); }
  .person__role { font-size: 13px; color: var(--silver-soft); letter-spacing: .5px; }
  .contacts {
    position: absolute;
    top: 274px;
    left: 22px;
    right: 22px;
    display: flex;
    justify-content: space-between;
    font-size: 10.5px;
    font-weight: 400;
    color: var(--silver);
    white-space: nowrap;
  }
  .contact { display: flex; align-items: center; gap: 5px; }
  .contact svg { width: 11px; height: 11px; fill: var(--silver); flex: none; }

  /* Back */
  .back-brand {
    position: absolute;
    top: 78px;
    left: 0;
    width: 100%;
    display: flex;
    justify-content: center;
    align-items: center;
    gap: 16px;
  }
  .back-brand__mark {
    width: 62px;
    height: 62px;
    border: 1.5px solid var(--silver);
  }
  .back-brand__name {
    font-weight: 300;
    font-size: 24px;
    letter-spacing: 1px;
    color: var(--silver);
  }
  .tagline {
    position: absolute;
    top: 190px;
    width: 100%;
    text-align: center;
    font-family: "Pinyon Script", cursive;
    font-size: 30px;
    color: var(--silver);
  }
</style>
</head>
<body>
  <section class="card card--front" aria-label="Card front">
    <div class="brand">
      <span class="brand__mark"></span>
      <div class="brand__name">PETER LANFORD</div>
      <div class="brand__sub">STUDIOS</div>
    </div>
    <div class="rule rule--top"></div>
    <div class="person">
      <span class="person__name">MARK ELLIS</span>
      <span class="person__dash">–</span>
      <span class="person__role">CEO/FOUNDER</span>
    </div>
    <div class="rule rule--bottom"></div>
    <div class="contacts">
      <span class="contact">
        <svg viewBox="0 0 24 24" aria-hidden="true"><path d="M6.6 10.8a15.2 15.2 0 0 0 6.6 6.6l2.2-2.2a1 1 0 0 1 1-.25 11.4 11.4 0 0 0 3.6.57 1 1 0 0 1 1 1V20a1 1 0 0 1-1 1A17 17 0 0 1 3 4a1 1 0 0 1 1-1h3.5a1 1 0 0 1 1 1c0 1.25.2 2.45.57 3.57a1 1 0 0 1-.25 1z"/></svg>
        555-418-2061
      </span>
      <span class="contact">
        <svg viewBox="0 0 24 24" aria-hidden="true"><path d="M2 5h20v14H2z M3.5 6.5 12 12.5l8.5-6z" fill-rule="evenodd"/></svg>
        petelanfordgallery@mailbox.example
      </span>
      <span class="contact">
        <svg viewBox="0 0 24 24" aria-hidden="true"><circle cx="12" cy="12" r="10"/></svg>
        lanfordgallery.snapfolio.example
      </span>
    </div>
  </section>

  <section class="card card--back" aria-label="Card back">
    <div class="back-brand">
      <span class="back-brand__mark"></span>
      <span class="back-brand__name">Peter Lanford Studios</span>
    </div>
    <div class="tagline">Wedding and Event Photography</div>
  </section>
</body>
</html>
```